Dallas Texas Special Event Center Flyer

Need a new brochure (small 8.5 x 11 tri-fold) for an event center in Dallas, Texas area. It is located on a golf course and is ideal for weddings, quinceaneras, retirement parties, etc. Is best known for weddings. There is no logo for the event center. I have attached the prior brochure, which is not professional. We do not have any site photos.

Target Market(s)

people seeking special event space in dallas, texas area. Brides, meeting planners, etc.

Industry/Entity Type

Golf Course

Font styles to use
Script
Other font styles liked:
• combine serif and some use of script ok

Requirements
Must have
• lots of photos - see attached

```html
<!DOCTYPE html>
<html lang="en">
<head>
<meta charset="utf-8">
<title>Event Center at Willowbend – Tri-fold Brochure</title>
<link rel="stylesheet" href="https://fonts.googleapis.com/css2?family=Open+Sans:wght@400;600&display=swap">
<style>
  :root{
    --page-bg:#e4e4e4;
    --brown-light:#7a3a1c;
    --brown-dark:#561d0e;
    --warm-1:#e6bd84;
    --warm-2:#c4874a;
    --warm-3:#8a4d24;
    --teal:#5fc2b4;
    --teal-soft:#a7e0d6;
    --plum:#6a2350;
    --gold:#e0b450;
    --white:#ffffff;
  }
  *{margin:0;padding:0;box-sizing:border-box}
  html,body{width:1200px;height:1080px;overflow:hidden;background:var(--page-bg)}
  .brochure{
    position:absolute;left:30px;top:100px;width:1140px;height:880px;
    background:linear-gradient(180deg,var(--brown-light) 0%,var(--brown-dark) 100%);
    overflow:hidden;font-family:"Open Sans",sans-serif;color:var(--white);
  }
  .artwork{position:absolute;inset:0}
  .fold{position:absolute;top:0;bottom:0;width:1px;background:rgba(0,0,0,.12)}
  .fold--one{left:380px}.fold--two{left:760px}
  .copy{position:absolute;font-size:14px;line-height:20px;text-shadow:0 1px 2px rgba(0,0,0,.35)}
  .copy p+p{margin-top:12px}
  .copy--intro{left:47px;top:76px;width:218px}
  .copy--bridal{left:20px;top:578px;width:140px;font-size:15px;line-height:23.5px}
  .copy--banquet{left:422px;top:530px;width:222px;font-size:14.5px;line-height:22px}
  .copy--kitchen{left:811px;top:248px;width:205px;line-height:22.5px}
  .venue-name{
    position:absolute;left:420px;top:44px;width:320px;
    font-family:"Open Sans",sans-serif;font-weight:600;font-size:28px;line-height:34px;
    color:var(--white);text-shadow:0 1px 3px rgba(0,0,0,.35);
  }
</style>
</head>
<body>
<main class="brochure">
  <svg class="artwork" width="1140" height="880" viewBox="0 0 1140 880" xmlns="http://www.w3.org/2000/svg">
    <defs>
      <linearGradient id="warm-photo" x1="0" y1="0" x2="1" y2="1">
        <stop offset="0" stop-color="var(--warm-2)"/>
        <stop offset=".45" stop-color="var(--warm-1)"/>
        <stop offset="1" stop-color="var(--warm-3)"/>
      </linearGradient>
      <linearGradient id="plum-wash" x1="0" y1="0" x2="0" y2="1">
        <stop offset="0" stop-color="var(--plum)" stop-opacity=".95"/>
        <stop offset="1" stop-color="var(--plum)" stop-opacity="0"/>
      </linearGradient>
      <linearGradient id="bride-photo" x1="0" y1="0" x2="0" y2="1">
        <stop offset="0" stop-color="#8e7c6c"/><stop offset="1" stop-color="#d8ccbd"/>
      </linearGradient>
      <linearGradient id="bouquet-photo" x1="0" y1="0" x2="1" y2="1">
        <stop offset="0" stop-color="#e7c3bf"/><stop offset="1" stop-color="#c99795"/>
      </linearGradient>
      <linearGradient id="cake-photo" x1="0" y1="0" x2="1" y2="0">
        <stop offset="0" stop-color="#9a8a80"/><stop offset=".6" stop-color="#e9e2dc"/><stop offset="1" stop-color="#3a2a26"/>
      </linearGradient>
      <radialGradient id="mic-photo"><stop offset="0" stop-color="#b9a894"/><stop offset="1" stop-color="#7c6c5c"/></radialGradient>
    </defs>

    <path class="plum-band" d="M560 320 C640 255 720 190 820 180 C950 170 1060 220 1140 294 L1140 560 L560 560 Z" fill="url(#plum-wash)"/>

    <path class="hero-photo" role="img" aria-label="Warm candlelit banquet table with a rose and eucalyptus centerpiece and crystal glasses"
      d="M0 0 H1140 V294 C1060 220 950 170 820 180 C720 190 640 255 560 320 C480 380 420 510 300 550 C200 580 60 520 0 305 Z"
      fill="url(#warm-photo)"/>
    <path class="swoosh" d="M0 305 C60 520 200 580 300 550 C420 510 480 380 560 320 C640 255 720 190 820 180 C950 170 1060 220 1140 294"
      fill="none" stroke="var(--teal)" stroke-width="6"/>
    <path d="M0 318 C62 530 200 590 302 560" fill="none" stroke="var(--teal-soft)" stroke-width="3" opacity=".7"/>

    <path class="bouquet-photo" role="img" aria-label="Bride and bridesmaids holding white bouquets"
      d="M851 38 H1088 V188 Q1088 218 1058 218 H811 V78 Q811 38 851 38 Z" fill="url(#bouquet-photo)" stroke="var(--white)" stroke-width="1"/>

    <circle class="mic-photo" role="img" aria-label="Microphone on a stand in a conference room" cx="653" cy="430" r="80" fill="url(#mic-photo)" stroke="var(--gold)" stroke-width="2"/>

    <path class="bride-photo" role="img" aria-label="Bride in a veil preparing in the bridal suite"
      d="M211 567 H378 V867 H171 V607 Q171 567 211 567 Z" fill="url(#bride-photo)"/>

    <path class="cake-photo" role="img" aria-label="Couple cutting a white wedding cake decorated with roses"
      d="M688 553 H1011 Q1111 553 1111 653 V845 H758 Q688 845 688 775 Z" fill="url(#cake-photo)" stroke="var(--white)" stroke-width="1"/>
  </svg>

  <div class="fold fold--one"></div>
  <div class="fold fold--two"></div>

  <h1 class="venue-name">Event Center at Willowbend</h1>

  <section class="copy copy--intro">
    <p>The Event Center at Willowbend offers a 12,000 square foot facility which boasts a Grand Ballroom and two Banquet rooms.</p>
    <p>The grand ballroom will accommodate 809 guests for a wedding ceremony and reception, quinceanera, retirement party or any occasion that demands a large-scale, elegant setting.</p>
  </section>

  <section class="copy copy--bridal">
    <p>The bridal suite at the top of the winding staircase allows the Bride and her bridesmaids to prepare for the big day out of sight of arriving guests, allowing a dramatic grand entrance.</p>
  </section>

  <section class="copy copy--banquet">
    <p>Banquet room 1 will accommodate 103 guests for a mid-size, private event such as a birthday or retirement party or company holiday party while Banquet room 2 will accommodate 35 guests for a small intimate event such as a bridal shower, bridesmaid’s luncheon or corporate training. The rooms can be used separately or together.</p>
  </section>

  <section class="copy copy--kitchen">
    <p>The event center has a full commercial kitchen onsite to cater any event from formal dining to buffet-style. The menu can be customized to your specifications and will be prepared by our expert chef and his team.</p>
    <p>The Event Center at Willowbend is the perfect location for your wedding, conference, seminar, party, reunion or graduation.</p>
  </section>
</main>
</body>
</html>
```